Corporate Design für lumavent capital partners (lcp)
Zielgruppe
Was wir machen:
Wir sind ein hochwertiger Finanzmakler, der seinen Mandaten in allen Bereichen zum Thema 'Finanzen und Versicherungen' mit Rat und Tat zur Seite steht. Vertrauen und Seriosität stehen dabei an erster Stelle.
Unsere Dienstleistung zielt darauf ab, der Ansprechpartner Nummer 1 zu sein, wenn es um Produkte aus dem Finanz- und Versicherungssektor geht. Gemäß dem Motto 'Ihr Plan bis zum Schluss'.
Somit müssen sich unsere Mandanten nicht mit verschiedenen Banken und Versicherern auseinandersetzen und haben mit uns einen Ansprechpartner für alle Belange. Nach einer intensiven Anaylse der Ist-Situation erarbeiten wir im jeweiligen Bereich die optimale Lösung heraus und fassen diese schriftlich in einem Gesamtkonzept für unsere Mandanten zusammen. Somit erhält er eine übersichtliche Handlungsempfehlung von uns.
--> Kurz gesagt: Wir erstellen maßgeschneiderte Finanzkonzepte für Privatkunden, sowie für Klein- und Mittelständische Unternehmen.
Unsere Zielgruppe:
Da unsere Beratung fachlich und inhaltlich sehr anspruchsvoll ist, haben wir überwiegend (angehende) Akademiker und Selbstständige/Unternehmer in unserem Bestand. Daher ist unsere Zielgruppe eher im 'gebildeten Bereich' zu suchen, ohne groß wertend klingen zu wollen. Die Altersspanne liegt vermehrt zwischen 25-45 jahren.
Neben den Akademikern und den Unternehmern betreuen wir zunehmend Klein- und Mittelständische Unternehmen im Bereich 'Betriebliches Vorsorgemanagement'.
--> Kurz gesagt: (Angehende) Akademiker, Selbstständige/Unternehmer, Klein- & Mittelständische Unternehmen
Wer wir sind:
Ein überwiegend junges und dynamisches Team aus 12 Leuten im Alter zwischen 22 und 38. Lediglich unser 'Senior' hat so gerade die 40er-Marke übersprungen. Jeder von uns ist hoch motiviert stets die optimale Lösung für seine Mandanten herauszuarbeiten.
Aufgabenstellung
Nach 14 Jahren bei der 'lumavent GmbH Makler', werden wir uns nun mit einem Teil des Teams "abspalten" und die 'lumavent capital partners' gründen.
Uns ist wichtig, dass mit dem Logo ein frischer Wind einhergeht und eine "Novation" zu erkennen ist. Dennoch soll weiterhin zu erkennen sein, dass wir nach wie vor im gleichen Sektor tätig sind und der Bruch nicht zu radikal ist.
Wir wollen also gerne nach wie vor als "lumavent" wahrgenommen werden, aber mit dem Logo muss klar werden, dass wir nicht mehr die alte "lumavent" sind. Diese wird nämlich nach wie vor bestehen bleiben, aber an anderen Standorten und mit leicht anderen Schwerpunkten ihre Mandaten beraten.
Wir werden in Hannover, Paderborn, Kassel und im Sauerland aktiv sein. Die alte lumavent in Köln, Magdeburg und Jena. Die Lösung wird also ein kleiner Drahtseilakt ;-)
Evtl. können Teile des alten Schriftzugs erhalten bleiben und mit neuer Farbe und dem Zusatz "financial services" verknüpft werden (Altes Logo ist beigefügt).
Die Farbe grün wird doch als neu und frisch wahrgenommen, oder?!
Wir sind aber auch gerne offen für alle anderen Ideen!!!

```html
<!DOCTYPE html>
<html lang="de">
<head>
<meta charset="utf-8">
<title>lumavent capital partners – Geschäftsausstattung</title>
<link href="https://fonts.googleapis.com/css2?family=Mulish:wght@300;400;600;800&display=swap" rel="stylesheet">
<style>
  :root{
    --bg:#f1f1f2;
    --paper:#ffffff;
    --green:#a6c80d;
    --green-light:#c5d400;
    --green-dark:#8fbe1e;
    --ink:#2b2b2b;
    --grey-window:#acacac;
    --shadow:0 6px 14px rgba(0,0,0,.16);
  }
  *{margin:0;padding:0;box-sizing:border-box}
  html,body{width:1200px;height:801px;overflow:hidden}
  body{background:linear-gradient(180deg,#f7f7f8 0%,var(--bg) 100%);font-family:"Mulish",sans-serif;color:var(--ink);position:relative}
  .wordmark{position:absolute;color:var(--green);font-family:"Mulish",sans-serif;font-weight:800;line-height:1;text-align:center}
  .wordmark .name{display:block;letter-spacing:-.01em}
  .wordmark .tag{display:block;letter-spacing:.06em}
  .hero-mark{left:177px;top:86px;width:295px}
  .hero-mark .name{font-size:78px}
  .hero-mark .tag{font-size:21px;margin-top:6px}
  .sheet{position:absolute;background:var(--paper);box-shadow:var(--shadow)}
  .card-front{left:58px;top:254px;width:259px;height:168px}
  .card-front .wordmark{left:50px;top:60px;width:159px}
  .card-front .name{font-size:40px}
  .card-front .tag{font-size:11px;margin-top:3px}
  .card-back{left:333px;top:254px;width:259px;height:168px;background:linear-gradient(180deg,var(--green-light) 0%,var(--green-dark) 100%);color:#fff}
  .card-back .person{position:absolute;left:78px;top:26px}
  .card-back .person b{display:block;font-weight:800;font-size:9px;letter-spacing:.03em}
  .card-back .person span{display:block;font-weight:300;font-size:8px;margin-top:1px}
  .card-back .divider{position:absolute;left:69px;top:60px;width:1px;height:53px;background:#fff}
  .card-back .contact{position:absolute;left:0;top:58px;list-style:none;width:100%}
  .card-back .contact li{height:21.5px;display:flex;align-items:center;font-size:8px;font-weight:300}
  .card-back .contact svg{width:10px;height:10px;margin-left:50px;margin-right:18px;fill:#fff}
  .envelope{left:58px;top:496px;width:536px;height:267px}
  .envelope .wordmark{left:50px;top:40px;width:138px}
  .envelope .name{font-size:32px}
  .envelope .tag{font-size:10px;margin-top:3px}
  .envelope .window{position:absolute;left:47px;top:121px;width:206px;height:111px;border-radius:10px;background:linear-gradient(135deg,#b9b9b9,#9f9f9f)}
  .letter{left:630px;top:34px;width:521px;height:737px;font-size:7px;line-height:1.5}
  .letter .wordmark{left:346px;top:44px;width:143px}
  .letter .name{font-size:30px}
  .letter .tag{font-size:10px;margin-top:2px}
  .fold{position:absolute;left:0;width:8px;height:1px;background:#333}
  .sender-line{position:absolute;left:62px;top:157px;font-size:5.5px}
  .recipient{position:absolute;left:62px;top:170px;font-size:8px;line-height:1.55}
  .info{position:absolute;right:32px;top:135px;text-align:right;font-size:6px;line-height:1.75}
  .info p+p{margin-top:5px}
  .subject{position:absolute;left:62px;top:245px}
  .body{position:absolute;left:62px;top:276px;width:420px}
  .body p{margin-bottom:10px}
  .letter-footer{position:absolute;left:0;bottom:0;width:100%;height:76px;background:linear-gradient(90deg,var(--green-light),var(--green-dark));color:#fff;font-size:6px;line-height:1.75}
  .letter-footer div{position:absolute;top:26px}
</style>
</head>
<body>

<div class="wordmark hero-mark"><span class="name">lumavent</span><span class="tag">capital partners</span></div>

<section class="sheet card-front">
  <div class="wordmark"><span class="name">lumavent</span><span class="tag">capital partners</span></div>
</section>

<section class="sheet card-back">
  <div class="person"><b>Max Mustermann</b><span>Position</span></div>
  <div class="divider"></div>
  <ul class="contact">
    <li><svg viewBox="0 0 24 24"><path d="M6.6 10.8a15 15 0 0 0 6.6 6.6l2.2-2.2c.3-.3.7-.4 1-.2 1.1.4 2.3.6 3.6.6.6 0 1 .4 1 1V20c0 .6-.4 1-1 1C10.6 21 3 13.4 3 4c0-.6.4-1 1-1h3.5c.6 0 1 .4 1 1 0 1.3.2 2.5.6 3.6.1.3 0 .7-.2 1z"/></svg>12345 67890</li>
    <li><svg viewBox="0 0 24 24"><path d="M12 2a10 10 0 1 0 5 18.7l-1-1.7A8 8 0 1 1 20 12v1.2c0 .9-.7 1.6-1.5 1.6S17 14 17 13.2V12a5 5 0 1 0-1.5 3.6A3.5 3.5 0 0 0 22 13.2V12A10 10 0 0 0 12 2zm0 13a3 3 0 1 1 0-6 3 3 0 0 1 0 6z"/></svg>mustermann@lumavent.de</li>
    <li><svg viewBox="0 0 24 24"><path d="M10.6 13.4a1 1 0 0 1 0-1.4l4-4a1 1 0 1 1 1.4 1.4l-4 4a1 1 0 0 1-1.4 0zM8.5 10.1 6.4 12.2a3 3 0 0 0 4.2 4.2l2.1-2.1 1.4 1.4-2.1 2.1a5 5 0 0 1-7-7l2.1-2.1zm7 3.8 2.1-2.1a3 3 0 0 0-4.2-4.2l-2.1 2.1-1.4-1.4L12 6.2a5 5 0 0 1 7 7l-2.1 2.1z"/></svg>www.lumavent-cp.de</li>
    <li><svg viewBox="0 0 24 24"><path d="M12 2a7 7 0 0 0-7 7c0 5 7 13 7 13s7-8 7-13a7 7 0 0 0-7-7zm0 9.5A2.5 2.5 0 1 1 12 6.5a2.5 2.5 0 0 1 0 5z"/></svg>Musterstr. 5, 45868 Muster</li>
  </ul>
</section>

<section class="sheet envelope">
  <div class="wordmark"><span class="name">lumavent</span><span class="tag">capital partners</span></div>
  <div class="window"></div>
</section>

<section class="sheet letter">
  <div class="wordmark"><span class="name">lumavent</span><span class="tag">capital partners</span></div>
  <span class="fold" style="top:260px"></span>
  <span class="fold" style="top:369px"></span>
  <span class="fold" style="top:520px"></span>

  <p class="sender-line">lumavent capital partners | Musterstraße 9 | 45868 Muster</p>
  <p class="recipient">Herr Mustermann<br>Musterstraße 3<br>48555 Muster</p>

  <div class="info">
    <p>lumavent capital partners<br>Musterstraße 9<br>45868 Muster</p>
    <p>Telefon: 0511 482730<br>Telefax: 0511 482731</p>
    <p>info@lumavent-cp.de<br>www.lumavent-cp.de</p>
  </div>

  <p class="subject">Hier steht eine Betreffzeile</p>

  <div class="body">
    <p>Sehr geehrte Frau Musterbeispiel,</p>
    <p>als Kunde unseres jungen und modernen Unternehmens erwartet<br>Sie Qualität in höchstem Maße.</p>
    <p>Sie können sicher zu sein, genau zu bekommen, was wir Ihnen versprechen.<br>Und damit werden Sie auch rundum zufrieden sein. Das garantieren wir Ihnen.</p>
    <p>Schauen Sie doch gleich das beiliegende Prospekt. Wir bieten Ihnen moderne und hochwertige Produkte, die auf dem neuesten Stand der Technik sind, an. Überzeugen Sie sich selbst von der hochwertigen Qualität unserer Produkte und bestellen Sie noch heute.</p>
    <p>Wir freuen uns auf Ihre Bestellung und sind bei Rückfragen gerne für Sie da.</p>
    <p>Mit freundlichen Grüßen</p>
  </div>

  <footer class="letter-footer">
    <div style="left:49px">lumavent capital partners<br>Musterstraße 9<br>45868 Muster</div>
    <div style="left:188px">USt-IDNR: DE4471209<br>Steuernummer: 174/415/062<br>Inhaber: Max Mustermann</div>
    <div style="left:364px">Sparkasse Musterstadt<br>IBAN: DE12 3456 0000 0000 7788<br>BIC: LUMADEXX12</div>
  </footer>
</section>

</body>
</html>
```